Brightvale, The Pixel Den or Coding for Kids

Brightvale
We build talent
We need a creative inspiring poster design for a new company based in Bahrain called 'Brightvale'. we teach children computer coding (game developments) and robotics in a play like environment. (activity-based not lectured based) which will develop kids talents in a challenging and enjoying way. (serious and fun)

we like and eye catching poster that will inspire kids to join our academy. Use vibrant color to create energy, elicit a mood and attract the eye.
The poster should be based on our value of:
Inspiration
learning is fun
knowledge is power

Relevant ideas were written on the image I attached.
Updates

Target Market(s)

Parents and KIds

Industry/Entity Type

Education

Logo Text

Brightvale, Building Talents

Font styles to use
Sans Serif

Colors
ec1f27
f37122
f78f20
ffc214
fbef40
9bcb3c
add136
33b8a4
33a6d7

Requirements
Must have
• looking for a design that when a parent see it: "I want to get my kid in to coding!"
• attractive,elegant,colorful,inspiring with a simple and strong message.

```html
<!DOCTYPE html>
<html lang="en">
<head>
<meta charset="utf-8">
<title>Brightvale – Page Timeline</title>
<link rel="stylesheet" href="https://fonts.googleapis.com/css2?family=Arimo:wght@400;700&family=Oswald:wght@500&display=swap">
<style>
:root{
  --top-blue:#3b5998;
  --notice-blue:#6f86b5;
  --link-blue:#3b5998;
  --link-bright:#365899;
  --page-bg:#e9eaed;
  --card-bg:#ffffff;
  --card-border:#d3d6db;
  --text-dark:#141823;
  --text-mid:#4b4f56;
  --text-light:#9197a3;
  --avatar:#c4cde0;
  --btn-bg:#f6f7f9;
  --btn-border:#ced0d4;
  --post-blue:#4e69a2;
  --brand-orange:#f78f20;
  --hl-yellow:#ffc214;
  --hl-lemon:#fbef40;
  --hl-orange:#f37122;
  --hl-teal:#33b8a4;
  --hl-blue:#33a6d7;
}
*{box-sizing:border-box;margin:0;padding:0}
html,body{width:1200px;height:893px;overflow:hidden;background:var(--page-bg)}
body{font-family:'Arimo',Arial,sans-serif;color:var(--text-dark);font-size:12px}
.stage{position:relative;width:1122px;height:835px;transform:scale(1.0695);transform-origin:0 0;background:var(--page-bg)}
.abs{position:absolute}

/* top bar */
.topbar{left:0;top:0;width:1122px;height:43px;background:linear-gradient(#4e69a2,var(--top-blue));border-bottom:1px solid #29447e}
.site-mark{left:75px;top:9px;width:24px;height:24px;background:#fff;border-radius:3px}
.search{left:105px;top:9px;width:400px;height:24px;background:#fff;border-radius:2px;display:flex;align-items:center;padding-left:7px;font-size:14px;color:#8d949e}
.search-btn{position:absolute;right:0;top:0;width:26px;height:24px;border-left:1px solid #dddfe2;display:flex;align-items:center;justify-content:center}
.notice{left:0;top:43px;width:1122px;height:27px;background:var(--notice-blue);color:#fff;font-size:12px;display:flex;align-items:center;justify-content:center}
.notice b{margin:0 3px}

/* admin nav */
.admin-nav{left:75px;top:70px;width:984px;height:45px;background:var(--card-bg);border:1px solid var(--card-border);border-top:none;display:flex;align-items:stretch;font-size:14px;color:var(--text-mid)}
.admin-nav .item{padding:0 17px;display:flex;align-items:center;border-right:1px solid #e5e5e5;position:relative}
.admin-nav .item.active{color:var(--text-dark);font-weight:700}
.admin-nav .item.active::after{content:"";position:absolute;left:16px;right:16px;bottom:0;height:3px;background:var(--link-blue)}
.admin-nav .spacer{flex:1}
.admin-nav .item.right{border-right:none;border-left:1px solid #e5e5e5}
.caret{font-size:8px;margin-left:7px}

/* cover */
.cover{left:75px;top:124px;width:850px;height:315px;background:linear-gradient(100deg,#4a4a4a 0%,#7a7773 40%,#8e8a84 60%,#5b5853 100%);overflow:hidden}
.cover-shade{left:75px;top:340px;width:850px;height:99px;background:linear-gradient(rgba(0,0,0,0),rgba(0,0,0,.55))}
.headline{left:240px;top:144px;width:310px;text-align:center;font-family:'Oswald','Arial Narrow',sans-serif;font-weight:500;text-transform:uppercase;white-space:nowrap;letter-spacing:1px;text-shadow:0 1px 2px rgba(0,0,0,.35)}
.headline .l1{display:block;font-size:40px;line-height:50px}
.headline .l2{display:block;font-size:29px;line-height:44px}
.headline .l3{display:block;font-size:30px;line-height:44px}
.c-yellow{color:var(--hl-yellow)}
.c-lemon{color:var(--hl-lemon)}
.c-orange{color:var(--hl-orange)}
.c-teal{color:var(--hl-teal)}
.c-blue{color:var(--hl-blue)}

.profile{left:89px;top:300px;width:170px;height:170px;background:#fff;border:1px solid #bdc1c9;border-radius:3px;display:flex;align-items:center;justify-content:center;gap:7px}
.profile .dot{width:13px;height:13px;border-radius:50%;background:var(--brand-orange)}
.profile .wordmark{font-size:22px;color:var(--brand-orange);letter-spacing:1.5px}
.page-name{left:270px;top:370px;color:#fff;font-size:23px;font-weight:700;text-shadow:0 0 3px rgba(0,0,0,.6)}
.page-sub{left:270px;top:403px;color:#fff;font-size:17px;text-shadow:0 0 3px rgba(0,0,0,.6)}
.btn{background:var(--btn-bg);border:1px solid var(--btn-border);border-radius:2px;height:28px;display:flex;align-items:center;font-size:12px;font-weight:700;color:var(--text-mid);padding:0 9px;gap:5px;white-space:nowrap}
.btn-liked{left:600px;top:399px;width:84px}
.btn-group{left:695px;top:399px;display:flex}
.btn-group .btn{border-radius:0}
.btn-group .btn + .btn{border-left:none}

/* tabs */
.tabs{left:75px;top:439px;width:850px;height:43px;background:var(--card-bg);border:1px solid var(--card-border);border-top:none;font-size:14px;color:var(--text-mid)}
.tab{position:absolute;top:0;height:43px;display:flex;align-items:center}
.tab.active{font-weight:700;color:var(--text-dark)}
.tab.active::after{content:"";position:absolute;left:-6px;right:-6px;bottom:-1px;height:3px;background:var(--link-blue)}
.tab-sep{position:absolute;top:0;width:1px;height:43px;background:#e5e5e5}

/* stats sidebar */
.stats{left:937px;top:124px;width:122px;height:291px;background:var(--card-bg);border:1px solid var(--card-border);text-align:center}
.stats h3{height:37px;display:flex;align-items:center;justify-content:center;font-size:12px;font-weight:700;background:#f6f7f9;border-bottom:1px solid #e5e5e5}
.stats h3.mid{border-top:1px solid #e5e5e5}
.stat{margin:0 10px;padding:14px 0 10px;border-bottom:1px solid #e5e5e5}
.stat.last{border-bottom:none}
.stat b{display:block;font-size:13px}
.stat span{font-size:11px;color:var(--link-blue)}
.years{left:937px;top:437px;width:100px;font-size:12px;color:var(--text-light)}
.years div{height:24px;display:flex;align-items:center;padding-left:8px;border-left:3px solid #d3d6db}
.years div.on{font-weight:700;color:#7f8591;border-left-color:#6d7583}

/* people */
.card{background:var(--card-bg);border:1px solid var(--card-border);border-radius:2px}
.people{left:75px;top:493px;width:328px;height:312px}
.people-head{height:38px;background:#f6f7f9;border-bottom:1px solid #e5e5e5;display:flex;align-items:center;justify-content:space-between;padding:0 11px;font-size:11px;font-weight:700;color:var(--text-mid)}
.people-count{height:44px;border-bottom:1px solid #e5e5e5;display:flex;align-items:center;justify-content:center;font-size:14px;color:var(--text-light)}
.people-count b{color:var(--text-dark);margin-right:4px}
.people-line{position:absolute;left:13px;top:97px;font-size:12px;color:var(--text-mid)}
.people-line b{color:var(--link-bright)}
.avatar{position:absolute;background:var(--avatar);overflow:hidden}
.plus{position:absolute;left:262px;top:123px;width:45px;height:44px;background:#e9ebf2;color:#7485ab;font-size:20px;font-weight:700;display:flex;align-items:center;justify-content:center}
.friend{position:absolute;left:13px;width:302px;height:40px;display:flex;align-items:center}
.friend .name{margin-left:48px;font-weight:700;color:var(--link-bright)}
.friend .btn{margin-left:auto;height:24px;font-size:12px}
.see-all{position:absolute;left:13px;top:287px;color:var(--link-bright)}

/* composer */
.composer{left:415px;top:493px;width:510px;height:312px;overflow:hidden}
.composer-tabs{height:36px;border-bottom:1px solid #e5e5e5;display:flex;align-items:center;padding-left:11px;gap:20px;font-size:12px;font-weight:700;color:var(--text-dark)}
.ctab{display:flex;align-items:center;gap:6px}
.ctab i{display:inline-block;width:15px;height:15px;border-radius:2px}
.composer-avatar{left:11px;top:49px;width:42px;height:42px}
.composer-text{left:64px;top:48px;width:424px;height:216px;font-size:14px;line-height:18px;color:var(--text-dark);overflow:hidden}
.composer-foot{position:absolute;left:0;bottom:0;width:100%;height:43px;border-top:1px solid #e5e5e5;background:#f6f7f9;display:flex;align-items:center;padding:0 12px;gap:22px}
.composer-foot .btn{margin-left:auto;height:24px}
.btn-post{height:24px;width:60px;background:var(--post-blue);border:1px solid #4267b2;color:#fff;font-weight:700;font-size:12px;border-radius:2px;display:flex;align-items:center;justify-content:center;margin-left:-6px}
</style>
</head>
<body>
<div class="stage">

  <header class="abs topbar"></header>
  <div class="abs site-mark"></div>
  <div class="abs search">Search for people, places and things
    <span class="search-btn"><svg width="12" height="12" viewBox="0 0 12 12"><circle cx="5" cy="5" r="3.8" fill="none" stroke="#9197a3" stroke-width="1.6"/><path d="M8 8l3 3" stroke="#9197a3" stroke-width="1.8"/></svg></span>
  </div>
  <div class="abs notice">You are posting, commenting and liking as <b>Your Page Name</b> — Change to Personal Profile</div>

  <nav class="abs admin-nav">
    <div class="item active">Page</div>
    <div class="item">Activity</div>
    <div class="item">Insights</div>
    <div class="item" style="border-right:none">Settings</div>
    <div class="spacer"></div>
    <div class="item right">Build Audience<span class="caret">▼</span></div>
    <div class="item right">Help<span class="caret">▼</span></div>
  </nav>

  <div class="abs cover" role="img" aria-label="Cover photo: a boy coding on a laptop in front of a wall of binary digits, with small doodles of a paper plane, robot and game pad"></div>
  <div class="abs cover-shade"></div>
  <h1 class="abs headline">
    <span class="l1"><span class="c-yellow">Bring your</span> <span class="c-teal">child</span></span>
    <span class="l2"><span class="c-orange">to learn</span> <span class="c-lemon">the language</span></span>
    <span class="l3"><span class="c-yellow">of the</span> <span class="c-blue">future</span></span>
  </h1>

  <div class="abs profile"><span class="dot"></span><span class="wordmark">Brightvale</span></div>
  <div class="abs page-name">BRIGHTVALE</div>
  <div class="abs page-sub">Kid developing games and app</div>

  <div class="abs btn btn-liked"><svg width="12" height="12" viewBox="0 0 12 12"><path d="M1 5h2v6H1zM4 5l3-4c1 0 1.5.6 1.3 1.6L8 4.5h2.6c.8 0 1.3.7 1.1 1.4l-1 4.2c-.2.6-.7.9-1.3.9H4z" fill="#4e69a2"/></svg>Liked<span class="caret">▼</span></div>
  <div class="abs btn-group">
    <div class="btn"><svg width="11" height="10" viewBox="0 0 11 10"><path d="M1 5l3 3 6-7" fill="none" stroke="#4b4f56" stroke-width="2"/></svg>Following</div>
    <div class="btn"><svg width="12" height="11" viewBox="0 0 12 11"><path d="M0 0h12v8H5l-3 3V8H0z" fill="#4b4f56"/></svg>Message</div>
    <div class="btn" style="width:52px;justify-content:center;font-size:16px;letter-spacing:1px">•••</div>
  </div>

  <div class="abs tabs">
    <div class="tab active" style="left:201px">Timeline</div>
    <div class="tab-sep" style="left:272px"></div>
    <div class="tab" style="left:292px">About</div>
    <div class="tab-sep" style="left:342px"></div>
    <div class="tab" style="left:362px">Photos</div>
    <div class="tab-sep" style="left:418px"></div>
    <div class="tab" style="left:438px">Likes</div>
    <div class="tab-sep" style="left:486px"></div>
    <div class="tab" style="left:505px">More<span class="caret">▼</span></div>
  </div>

  <aside class="abs stats">
    <h3>THIS WEEK</h3>
    <div class="stat"><b>999</b><span>Page Likes</span></div>
    <div class="stat last"><b>999</b><span>Post Reach</span></div>
    <h3 class="mid">UNREAD</h3>
    <div class="stat"><b>999</b><span>Notifications</span></div>
    <div class="stat last"><b>999</b><span>Messages</span></div>
  </aside>

  <div class="abs years">
    <div class="on">Recent</div><div>2013</div><div>2012</div><div>2011</div><div>2010</div>
  </div>

  <section class="abs card people">
    <div class="people-head">PEOPLE<svg width="9" height="12" viewBox="0 0 9 12"><path d="M1.5 1l5 5-5 5" fill="none" stroke="#4b4f56" stroke-width="2"/></svg></div>
    <div class="people-count"><b>999</b> likes</div>
    <div class="people-line"><b>Example person</b>, and <b>99 others</b> like this.</div>
    <div class="avatar" style="left:12px;top:123px;width:45px;height:44px" role="img" aria-label="Profile placeholder"></div>
    <div class="avatar" style="left:62px;top:123px;width:45px;height:44px" role="img" aria-label="Profile placeholder"></div>
    <div class="avatar" style="left:112px;top:123px;width:45px;height:44px" role="img" aria-label="Profile placeholder"></div>
    <div class="avatar" style="left:162px;top:123px;width:45px;height:44px" role="img" aria-label="Profile placeholder"></div>
    <div class="avatar" style="left:212px;top:123px;width:45px;height:44px" role="img" aria-label="Profile placeholder"></div>
    <div class="plus">+99</div>
    <div class="avatar" style="left:12px;top:178px;width:40px;height:40px" role="img" aria-label="Profile placeholder"></div>
    <div class="friend" style="top:178px"><span class="name">Example person</span><span class="btn">Invite</span></div>
    <div class="avatar" style="left:12px;top:229px;width:40px;height:40px" role="img" aria-label="Profile placeholder"></div>
    <div class="friend" style="top:229px"><span class="name">Example person</span><span class="btn">Invite</span></div>
    <div class="see-all">See All Friends</div>
  </section>

  <section class="abs card composer">
    <div class="composer-tabs">
      <span class="ctab"><i style="background:#5b7bc0"></i>Status</span>
      <span class="ctab"><i style="background:#f0a860"></i>Photo / Video</span>
      <span class="ctab"><i style="background:#fff;border:1px solid #6d7583"></i>Event, Milestone +</span>
    </div>
    <div class="abs avatar composer-avatar" role="img" aria-label="Profile placeholder"></div>
    <p class="abs composer-text">Lorem ipsum dolor sit amet, consectetur adipiscing elit. Etiam sit amet ante nisi, sit amet fermentum erat. Suspendisse vel nunc a massa consequat iaculis. Sed pellentesque vehicula elit. Mauris sodales mollis molestie. Integer ultrices laoreet ante, et faucibus sem cursus non. Suspendisse laoreet suscipit vestibulum. Integer mi augue, hendrerit ut fermentum ut, accumsan eget justo. Nam fringilla dapibus risus sed consequat. Nullam lacus urna, pellentesque et laoreet sit amet, volutpat sit amet dolor. Praesent a ultrices velit. Nulla facilisi. Ut sagittis dapibus bibendum. Proin id enim eros. Curabitur tincidunt lorem sed purus semper vitae tincidunt purus aliquet. Integer nulla metus, vestibulum at tincidunt at, euismod sed ligula. Vestibulum ante ipsum primis in faucibus orci</p>
    <div class="composer-foot">
      <svg width="16" height="16" viewBox="0 0 16 16"><circle cx="8" cy="8" r="6.5" fill="none" stroke="#90949c" stroke-width="1.6"/><path d="M8 4v4l3 2" fill="none" stroke="#90949c" stroke-width="1.6"/></svg>
      <svg width="12" height="16" viewBox="0 0 12 16"><path d="M6 15S1 9 1 6a5 5 0 0 1 10 0c0 3-5 9-5 9z" fill="#90949c"/><circle cx="6" cy="6" r="2" fill="#f6f7f9"/></svg>
      <svg width="16" height="14" viewBox="0 0 16 14"><path d="M1 3h4l1.5-2h3L11 3h4v10H1z" fill="#90949c"/><circle cx="8" cy="8" r="3" fill="#f6f7f9"/></svg>
      <span class="btn">Boost Post<span class="caret" style="margin-left:2px">▼</span></span>
      <span class="btn-post">Post</span>
    </div>
  </section>

</div>
</body>
</html>
```